New Business Cards for MB&LR

We need updated business cards for a staff of 15 engineers, estimators, project managers, and sales people. We have recently begun changes to our website and marketing material to improve our look and branding. We are an established fabricator specializing in pressure vessels, tanks, and structural steel. The owners require us to use the existing logo and old english text design. Also, we prefer dark grey or mostly black cards.
Target Market(s)
Engineers, purchasing agents, estimators, and project managers of; mining companies, refineries, industrial construction professionals
Industry/Entity Type
Business
Contact Information for Business Card
Logo, phone, website, email, etc.
Look and feel

```html
<!DOCTYPE html>
<html lang="en">
<head>
<meta charset="utf-8">
<title>MB&amp;LR Business Cards</title>
<link rel="stylesheet" href="https://fonts.googleapis.com/css2?family=Arimo&family=Tinos&family=UnifrakturMaguntia&display=swap">
<style>
  :root {
    --ink: #000000;
    --paper: #ffffff;
    --stage: #ffffff;
    --grey-text: #8a8a8a;
    --label-grey: #7a7a7a;
    --body-text: #1a1a1a;
    --card-shadow: rgba(0, 0, 0, 0.28);
  }
  * { box-sizing: border-box; margin: 0; padding: 0; }
  html, body {
    width: 759px;
    height: 1200px;
    overflow: hidden;
    background: var(--stage);
  }
  .canvas {
    position: relative;
    width: 759px;
    height: 1200px;
  }
  .card {
    position: absolute;
    overflow: hidden;
  }
  .card__bands {
    position: absolute;
    left: 0;
    top: 0;
    width: 100%;
    height: 100%;
  }
  .card--front {
    left: 52px;
    top: 69px;
    width: 482px;
    height: 268px;
    background: var(--ink);
  }
  .card--back {
    left: 228px;
    top: 380px;
    width: 486px;
    height: 269px;
    background: var(--paper);
    box-shadow: 0 1px 6px var(--card-shadow);
  }
  .brand-name {
    position: absolute;
    left: 0;
    width: 100%;
    text-align: center;
    font-family: "Tinos", serif;
    font-weight: 400;
    line-height: 1;
  }
  .card--front .brand-name {
    top: 100px;
    font-size: 52px;
    color: var(--paper);
    letter-spacing: 2px;
  }
  .card--back .brand-name {
    top: 52px;
    font-size: 34px;
    color: var(--ink);
    letter-spacing: 1px;
  }
  .web-address {
    position: absolute;
    left: 0;
    width: 100%;
    text-align: center;
    line-height: 1;
  }
  .card--front .web-address {
    top: 224px;
    font-family: "Arimo", sans-serif;
    font-size: 15px;
    color: var(--paper);
  }
  .card--back .web-address {
    top: 226px;
    font-family: "Tinos", serif;
    font-size: 16px;
    color: var(--ink);
  }
  .company-name {
    position: absolute;
    top: 126px;
    left: 0;
    width: 100%;
    text-align: center;
    font-family: "UnifrakturMaguntia", serif;
    font-size: 22px;
    color: var(--grey-text);
    line-height: 1;
  }
  .contact {
    position: absolute;
    top: 170px;
    left: 0;
    width: 100%;
    text-align: center;
    font-family: "Tinos", serif;
    font-size: 16px;
    line-height: 20px;
    color: var(--body-text);
  }
  .contact__label { color: var(--label-grey); }
</style>
</head>
<body>
<main class="canvas">

  <section class="card card--front" aria-label="Business card front">
    <svg class="card__bands" viewBox="0 0 482 268" aria-hidden="true">
      <polygon points="0,218 148,218 162,244 0,244" fill="var(--paper)"/>
      <polygon points="320,218 482,218 482,244 306,244" fill="var(--paper)"/>
    </svg>
    <p class="brand-name">MB&amp;LR</p>
    <p class="web-address">www.mbandlr.com</p>
  </section>

  <section class="card card--back" aria-label="Business card back">
    <svg class="card__bands" viewBox="0 0 486 269" aria-hidden="true">
      <polygon points="0,223 152,223 166,244 0,244" fill="var(--ink)"/>
      <polygon points="348,223 486,223 486,244 334,244" fill="var(--ink)"/>
    </svg>
    <p class="brand-name">MB&amp;LR</p>
    <p class="company-name">Midland Beam &amp; Layered Rolling</p>
    <div class="contact">
      <p><span class="contact__label">P:</span> 801-555-0147</p>
      <p><span class="contact__label">M:</span> jordan@mbandlr.com</p>
    </div>
    <p class="web-address">www.mbandlr.com</p>
  </section>

</main>
</body>
</html>
```